SUMMIT GATHERING 2021. August 20th -22nd.

The Hosts of the conference: Grace Tabernacle-Pastors Ron n Della ( Picture with two persons)

Guest Minister: Bishop Lucinda Okotieno. (Cedar Ridge Awakening)

Venue:
Sealand Gateway Lodgeview. 4817 North 239th Avenue Seattle, WA 98174.

Conference times.
Friday August 20th 6pm-8:30pm
Saturday August 21st. 6pm-8:30pm

Sunday August 22nd 10am-1pm
“ CHURCH RENEWAL GATHERING”

5pm-7:30pm
TWOFOLD SURGE GATHERING.

Target Market(s)

18-55

Industry/Entity Type

Religious/ Entertainment.

Requirements
Must have
• A highlight of the Relaunch service on Sunday August 22nd 5pm-7:30pm.
Nice to have
• Excellent ideas….

```html
<!DOCTYPE html>
<html lang="en">
<head>
<meta charset="utf-8">
<title>Summit Gathering 2021 – Grace Tabernacle</title>
<link rel="stylesheet" href="https://fonts.googleapis.com/css2?family=Montserrat:wght@800;900&family=Roboto:wght@700&family=Great+Vibes&display=swap">
<style>
  :root {
    --red: #c6422b;
    --red-deep: #ad3325;
    --red-text: #b3372b;
    --gold: #f7c51b;
    --white: #ffffff;
    --paper: #dedee2;
    --grey-light: #bdbdc0;
    --grey-dark: #8d8e93;
    --ink: #1d1b1b;
  }
  * { margin: 0; padding: 0; box-sizing: border-box; }
  html, body { width: 1200px; height: 1200px; overflow: hidden; background: var(--paper); }
  .poster { position: relative; width: 1200px; height: 1200px; overflow: hidden;
    background: linear-gradient(180deg, #d9d9dd 0%, #cfcfd4 100%); }

  .red-panel { position: absolute; left: 0; top: 0; width: 822px; height: 877px; }

  .brand { position: absolute; left: 65px; top: 130px; display: flex; align-items: center; gap: 10px; }
  .brand-square { width: 22px; height: 22px; background: var(--red); }
  .brand-name { font-family: 'Montserrat', sans-serif; font-weight: 800; font-size: 19px;
    color: var(--ink); letter-spacing: 0.5px; }

  .service { position: absolute; left: 362px; color: var(--white);
    font-family: 'Montserrat', sans-serif; font-weight: 900; line-height: 1; }
  .service-title { font-size: 38px; letter-spacing: -0.5px; }
  .service-row { display: flex; align-items: center; gap: 14px; margin-top: 8px; }
  .service-date { font-family: 'Montserrat', sans-serif; font-weight: 800; font-size: 14px;
    color: var(--gold); line-height: 1.35; letter-spacing: 0.2px; }
  .service--renewal { top: 150px; }
  .service--surge { top: 286px; }

  .photo { position: absolute; }
  .photo--hosts { left: 822px; top: 0; width: 378px; height: 877px;
    background: linear-gradient(160deg, #c9c8cf 0%, #a9a5ab 40%, #6b5a55 75%, #d8d4d6 100%); }
  .photo--guest { left: 0; top: 462px; width: 334px; height: 415px;
    border-radius: 140px 160px 0 0;
    background: linear-gradient(170deg, #3a2a24 0%, #7a5a48 35%, #e9dce0 60%, #6d6d6d 100%); }

  .label-card { position: absolute; background: var(--white); text-align: center;
    display: flex; flex-direction: column; align-items: center; justify-content: center; }
  .label-card--hosts { left: 283px; top: 461px; width: 539px; height: 121px; }
  .label-card--guest { left: 334px; top: 717px; width: 439px; height: 121px; }
  .label-script { font-family: 'Great Vibes', cursive; color: var(--red-text);
    font-size: 50px; line-height: 1.05; }
  .label-name { font-family: 'Montserrat', sans-serif; font-weight: 800; font-size: 15px;
    color: var(--gold); letter-spacing: 0.6px; margin-top: 8px; padding-bottom: 1px;
    border-bottom: 1.5px solid var(--red-text); }

  .times-band { position: absolute; left: 0; top: 877px; width: 1200px; height: 245px;
    background: linear-gradient(180deg, var(--grey-light) 0%, #a7a8ac 50%, var(--grey-dark) 100%); }
  .band-dots { position: absolute; right: 62px; top: 16px; display: flex; gap: 10px; }
  .band-dots span { width: 13px; height: 13px; border-radius: 50%; background: #e4e4e6; }
  .times-box { position: absolute; left: 252px; top: 42px; width: 660px; height: 170px;
    border: 2.5px solid var(--red); border-radius: 32px; text-align: center;
    font-family: 'Roboto', sans-serif; font-weight: 700; }
  .times-title { color: var(--gold); font-size: 44px; margin-top: 14px; line-height: 1; }
  .times-line { color: var(--white); font-size: 30px; line-height: 1.3; }
  .times-line:first-of-type { margin-top: 8px; }

  .venue-bar { position: absolute; left: 0; top: 1122px; width: 1200px; height: 78px;
    background: linear-gradient(90deg, var(--red-deep) 0%, var(--red) 50%, var(--red-deep) 100%);
    display: flex; align-items: center; justify-content: center;
    font-family: 'Roboto', sans-serif; font-weight: 700; font-size: 25px; color: var(--white); }
</style>
</head>
<body>
<main class="poster">
  <svg class="red-panel" width="822" height="877" viewBox="0 0 822 877" aria-hidden="true">
    <defs>
      <linearGradient id="panelRed" x1="0" y1="0" x2="0" y2="1">
        <stop offset="0" stop-color="#c9432b"/>
        <stop offset="1" stop-color="#b53828"/>
      </linearGradient>
    </defs>
    <polygon points="425,0 822,0 822,877 0,877" fill="url(#panelRed)"/>
  </svg>

  <div class="brand">
    <span class="brand-square"></span>
    <span class="brand-name">GRACE TABERNACLE</span>
  </div>

  <section class="service service--renewal">
    <div class="service-title">CHURCH RENEWAL</div>
    <div class="service-row">
      <span class="service-title">GATHERING</span>
      <span class="service-date">SUNDAY AUGUST<br>22ND 10AM-1PM</span>
    </div>
  </section>

  <section class="service service--surge">
    <div class="service-title">TWOFOLD SURGE</div>
    <div class="service-row">
      <span class="service-title">GATHERING</span>
      <span class="service-date">SUNDAY AUGUST<br>22ND 5PM-7:30PM</span>
    </div>
  </section>

  <div class="photo photo--hosts" role="img" aria-label="Photo of the host pastors, a smiling couple embracing"></div>
  <div class="photo photo--guest" role="img" aria-label="Portrait of the guest minister in a houndstooth blazer"></div>

  <div class="label-card label-card--hosts">
    <div class="label-script">The Hosts of the conference</div>
    <div class="label-name">GRACE TABERNACLE-PASTORS RON N DELLA</div>
  </div>

  <div class="label-card label-card--guest">
    <div class="label-script">Guest Minister</div>
    <div class="label-name">BISHOP LUCINDA OKOTIENO</div>
  </div>

  <section class="times-band">
    <div class="band-dots"><span></span><span></span><span></span></div>
    <div class="times-box">
      <div class="times-title">CONFERENCE TIMES.</div>
      <div class="times-line">FRIDAY AUGUST 20TH 6PM-8:30PM</div>
      <div class="times-line">SATURDAY AUGUST 21ST. 6PM-8:30PM</div>
    </div>
  </section>

  <footer class="venue-bar">SEALAND GATEWAY LODGEVIEW. 4817 NORTH 239TH AVENUE SEATTLE, WA 98174.</footer>
</main>
</body>
</html>
```